Packaging design for a Deli Shop "TERU Gourmet"

We need a packaging design for a new Deli Business we are opening soon. We produce food to be packaged and sold either fresh or frozen in transparent disposable plastic boxes, cardboard boxes and finally delivered in a bag (Paper, plastic or shopping bag whatever goes best with the design) to take out. The food we generally pack are salads, lasagnas, ceviches, sandwiches, cookies, granola, dips, etc.

The name of the company is "TERU Gourmet" Check our website for reference: www.terugourmet-example.com

We have a logo and a name we want to maintain (attached).

The product will be sold in our new deli store, that is inspired in big cities delikatessen, quite modern and trendy. It also delivers a message that everything we sell is high quality, artisan (not massive or mainstream) and great in flavors.

Packaging must communicate freshness, great flavor, high quality and high price.

Packaging must be feasible to produce and print easily without any complex or impossible to implement packaging, (preferrable to be done or easy to adapt from generic packaging).

All our communication will be in Spanish so please do not depend on english for the design. If english or any other language is used, please be sure its understandable in almost any country (ie Basic English, Italian).

Same packaging (labeling or boxes and bags) will be used, just changing the name of the product inside according to the product.

Most of our product will be displayed in refrigerators and freezers.
Updates

I just uploaded a visual brief of the packaging examples we would like to have.

Looking forward to see your designs.
Thank you

Reason: Some designers who said will participate havent submitted their deaigns, and still what is being submitted is not fully complying with the requirements. Thank you

Target Market(s)

The main target is High SEL, between 24 and 40, mostly woman

Industry/Entity Type

Communication

Requirements
Must have

Nice to have
• Please take a look at my website www.terugourmet-example.com to see the kind of coloring we are aiming to have.

Give the impression of being "Green"...

Include "Kraft" color paper / Brown paper color
Should not have
• Complex packaging difficult to implement in a simple print shop.
Expensive items.

```html
<!DOCTYPE html>
<html lang="es">
<head>
<meta charset="utf-8">
<title>TERU Gourmet – Empaque</title>
<link href="https://fonts.googleapis.com/css2?family=Marcellus+SC&family=Roboto:wght@700&display=swap" rel="stylesheet">
<style>
  :root{
    --brand-red:#c8371f;
    --orange:#e4572a;
    --green:#8cc43c;
    --yellow:#f0aa2c;
    --kraft:#b48a5e;
    --paper:#ffffff;
    --paper-edge:#dcdcdc;
    --bg:#ffffff;
  }
  html,body{margin:0;padding:0;overflow:hidden;}
  body{width:1200px;height:883px;background:var(--bg);position:relative;font-family:"Roboto",Arial,sans-serif;}

  /* ---------- bands with oval label ---------- */
  .band{position:absolute;height:40px;}
  .band__fill{position:absolute;inset:0;}
  .band--orange .band__fill{background:var(--orange);}
  .band--green .band__fill{background:var(--green);}
  .band--yellow .band__fill{background:var(--yellow);}

  .oval-label{
    position:absolute;width:166px;height:112px;top:50%;left:50%;
    transform:translate(-50%,-50%);
    background:var(--paper);border:2px solid var(--brand-red);border-radius:50%;
    box-shadow:0 0 0 3px var(--paper);
    display:flex;flex-direction:column;align-items:center;justify-content:center;
    color:var(--brand-red);text-align:center;
  }
  .oval-label__name{font-family:"Marcellus SC",Georgia,serif;font-size:28px;line-height:26px;letter-spacing:1px;display:flex;align-items:center;gap:6px;}
  .oval-label__name small{display:block;font-size:10px;letter-spacing:3px;line-height:11px;}
  .oval-label__square{width:12px;height:12px;background:var(--green);}
  .oval-label__tel{font-size:10px;line-height:11px;margin-top:5px;}
  .oval-label__web{font-size:8px;line-height:10px;}

  /* ---------- bags ---------- */
  .bag{position:absolute;width:292px;height:330px;top:515px;border:1px solid var(--paper-edge);}
  .bag--white{background:var(--paper);}
  .bag--kraft{background:var(--kraft);border-color:var(--kraft);}
  .bag__handle{position:absolute;left:50px;top:-64px;width:190px;height:80px;overflow:visible;}
  .bag__base{position:absolute;left:0;right:0;bottom:0;height:44px;}
  .bag--orange .bag__base{background:var(--orange);}
  .bag--yellow .bag__base{background:var(--yellow);}
  .bag--green .bag__base{background:var(--green);}
  .bag__brand{position:absolute;left:10px;bottom:52px;font-family:"Marcellus SC",Georgia,serif;line-height:1;}
  .bag__brand-name{font-size:50px;letter-spacing:1px;}
  .bag__brand-sub{font-size:14px;letter-spacing:5px;border-top:1px solid currentColor;margin-top:2px;padding-top:2px;}
  .bag--orange .bag__brand{color:var(--orange);}
  .bag--yellow .bag__brand{color:var(--yellow);}
  .bag--green .bag__brand{color:var(--green);}
</style>
</head>
<body>

<!-- Box band -->
<div class="band band--orange" style="left:70px;top:190px;width:440px;">
  <div class="band__fill" role="img" aria-label="Banda naranja con patrón de arabescos claros"></div>
  <div class="oval-label">
    <div class="oval-label__name"><span class="oval-label__square"></span><span>TERU<small>GOURMET</small></span></div>
    <div class="oval-label__tel">Tel. (507) 555-0142</div>
    <div class="oval-label__web">www.terugourmet-example.com</div>
  </div>
</div>

<!-- Band set -->
<div class="band band--orange" style="left:555px;top:60px;width:645px;">
  <div class="band__fill" role="img" aria-label="Banda naranja con patrón de arabescos claros"></div>
  <div class="oval-label" style="left:330px;">
    <div class="oval-label__name"><span class="oval-label__square"></span><span>TERU<small>GOURMET</small></span></div>
    <div class="oval-label__tel">Tel. (507) 555-0142</div>
    <div class="oval-label__web">www.terugourmet-example.com</div>
  </div>
</div>
<div class="band band--green" style="left:555px;top:205px;width:645px;">
  <div class="band__fill" role="img" aria-label="Banda verde con patrón de arabescos claros"></div>
  <div class="oval-label" style="left:330px;">
    <div class="oval-label__name"><span class="oval-label__square"></span><span>TERU<small>GOURMET</small></span></div>
    <div class="oval-label__tel">Tel. (507) 555-0142</div>
    <div class="oval-label__web">www.terugourmet-example.com</div>
  </div>
</div>
<div class="band band--yellow" style="left:555px;top:350px;width:645px;">
  <div class="band__fill" role="img" aria-label="Banda amarilla con patrón de arabescos claros"></div>
  <div class="oval-label" style="left:330px;">
    <div class="oval-label__name"><span class="oval-label__square"></span><span>TERU<small>GOURMET</small></span></div>
    <div class="oval-label__tel">Tel. (507) 555-0142</div>
    <div class="oval-label__web">www.terugourmet-example.com</div>
  </div>
</div>

<!-- Bags -->
<div class="bag bag--white bag--orange" style="left:110px;">
  <svg class="bag__handle" viewBox="0 0 190 80"><path d="M20 78 C20 0 90 0 90 60 M100 78 C100 0 170 0 170 60" fill="none" stroke="var(--orange)" stroke-width="9" stroke-linecap="round"/></svg>
  <div class="bag__brand"><div class="bag__brand-name">TERU</div><div class="bag__brand-sub">GOURMET</div></div>
  <div class="bag__base"></div>
</div>

<div class="bag bag--kraft bag--yellow" style="left:425px;">
  <svg class="bag__handle" viewBox="0 0 190 80"><path d="M20 78 C20 0 90 0 90 60 M100 78 C100 0 170 0 170 60" fill="none" stroke="var(--yellow)" stroke-width="9" stroke-linecap="round"/></svg>
  <div class="bag__brand"><div class="bag__brand-name">TERU</div><div class="bag__brand-sub">GOURMET</div></div>
  <div class="bag__base"></div>
</div>

<div class="bag bag--white bag--green" style="left:745px;">
  <svg class="bag__handle" viewBox="0 0 190 80"><path d="M20 78 C20 0 90 0 90 60 M100 78 C100 0 170 0 170 60" fill="none" stroke="var(--green)" stroke-width="9" stroke-linecap="round"/></svg>
  <div class="bag__brand"><div class="bag__brand-name">TERU</div><div class="bag__brand-sub">GOURMET</div></div>
  <div class="bag__base"></div>
</div>

</body>
</html>
```